Cadenza Elite Keyboard Academy is a comprehensive piano studio located in CBD area and provide individual piano lessons.

We also provide services for wedding organising band, or instrumental hiring or venue hiring, or organise concert to students.

I want my name card to be very creative, does not have to be the form or shape with the normal name card, can be in different shape. Also, I want the name card to be very upper class, because learning piano is a serious thing, so I do not want people to bargain with the prices. I want people to see it as a very elegant tuition so that they do not want to bargain and think it is worth to try.

Further more, Cadenza Elite Keyboard Academy is not like normal piano studio only provide piano lessons, we provide band services for each other event, such as cruise party, wedding etc. I want people to see it as owner of Elite Keyboard Academy, they will have different type of services all in one, I provide more than that, and I am well connected. I do not provide only piano lesson, but also all other musical knowledge and I am very professional

I want name card to be very simple, just name of company name, my name and website that's all, maybe phone number and email as well.

Please check my website to have more ideal concept.
http://harrietdowse.sitebuilder-example.com/cadenzakeyboard
Updates

Target Market(s)

For all people who love to play piano (better with upper class)

Industry/Entity Type

Wedding

Contact Information for Business Card

Harriet Dowse
Mobile:0418769052
Email: cadenzaelitekeys@mailbox-example.com

Colors

Designer to choose colors to be used in the design.

Requirements
Must have
• Creativity
Nice to have
• Black and white
some sort of piano image
Should not have
• Childish

```html
<!DOCTYPE html>
<html lang="en">
<head>
<meta charset="utf-8">
<title>Cadenza Elite Keyboard Academy — Business Card</title>
<link rel="stylesheet" href="https://fonts.googleapis.com/css2?family=Arimo:wght@400;700&display=swap">
<style>
  :root {
    --stage: #dcdcdc;
    --card: #ffffff;
    --ink: #111111;
    --charcoal: #1c1c1c;
    --crimson: #9b1b20;
    --key-light: #f4f4f4;
    --key-shade: #bdbdbd;
    --rule: #555555;
  }
  * { box-sizing: border-box; margin: 0; padding: 0; }
  html, body {
    width: 1200px; height: 985px; overflow: hidden;
    background: var(--stage);
    font-family: "Arimo", Arial, sans-serif;
  }
  .stage {
    width: 1200px; height: 985px;
    display: flex; flex-direction: column; align-items: center; justify-content: center;
    gap: 40px;
  }
  .card {
    position: relative;
    width: 820px; height: 430px;
    background: var(--card);
    border-radius: 26px;
    overflow: hidden;
    box-shadow: 0 6px 18px rgba(0,0,0,0.18);
  }

  /* Front */
  .front-brand {
    position: absolute; left: 0; right: 0; top: 0; height: 326px;
    display: flex; align-items: center; justify-content: center; gap: 26px;
  }
  .brand-square {
    width: 70px; height: 70px; background: var(--crimson);
  }
  .brand-name {
    font-weight: 700; font-size: 40px; line-height: 1.15; color: var(--ink);
  }
  .front-stripe {
    position: absolute; left: 0; right: 0; top: 326px; height: 10px;
    background: var(--crimson);
  }
  .front-band {
    position: absolute; left: 0; right: 0; bottom: 0; height: 94px;
    background: var(--charcoal);
    display: flex; align-items: center; padding-left: 60px;
  }
  .front-url {
    color: #ffffff; font-weight: 700; font-size: 19px; letter-spacing: 0.3px;
  }

  /* Back */
  .back-band-top, .back-band-bottom {
    position: absolute; left: 0; right: 0; background: var(--crimson);
  }
  .back-band-top { top: 0; height: 30px; }
  .back-band-bottom { bottom: 0; height: 50px; }
  .keyboard-art {
    position: absolute; left: 0; top: 30px; bottom: 50px; width: 290px;
    background: linear-gradient(90deg, var(--key-shade) 0%, var(--key-light) 55%, #ffffff 100%);
    border-right: 1.5px solid var(--rule);
  }
  .contact {
    position: absolute; left: 290px; right: 0; top: 30px; bottom: 50px;
    display: flex; flex-direction: column; align-items: center; justify-content: center;
    text-align: center; gap: 6px; padding: 0 16px;
  }
  .contact-company {
    color: var(--crimson); font-weight: 700; font-size: 26px; margin-bottom: 4px;
  }
  .contact-person {
    color: var(--ink); font-weight: 700; font-size: 30px; margin-bottom: 6px;
  }
  .contact-line {
    color: var(--ink); font-weight: 700; font-size: 19px;
  }
  .contact-line.url { font-size: 15px; }
</style>
</head>
<body>
  <main class="stage">
    <section class="card card-front">
      <div class="front-brand">
        <div class="brand-square"></div>
        <div class="brand-name">Cadenza Elite<br>Keyboard Academy</div>
      </div>
      <div class="front-stripe"></div>
      <div class="front-band">
        <span class="front-url">http://harrietdowse.sitebuilder-example.com/cadenzakeyboard</span>
      </div>
    </section>

    <section class="card card-back">
      <div class="back-band-top"></div>
      <div class="keyboard-art" role="img" aria-label="Piano keyboard illustration with black and white keys"></div>
      <div class="contact">
        <p class="contact-company">Cadenza Elite Keyboard Academy</p>
        <p class="contact-person">Harriet Dowse</p>
        <p class="contact-line">Mobile:0418769052</p>
        <p class="contact-line">cadenzaelitekeys@mailbox-example.com</p>
        <p class="contact-line url">http://harrietdowse.sitebuilder-example.com/cadenzakeyboard</p>
      </div>
      <div class="back-band-bottom"></div>
    </section>
  </main>
</body>
</html>
```